bryn calvo website design

An IT support and IT Security Company - just use dummy text for now for the design. Examples of sites we like the looks and feel of but need it more professional feel are like: www.quorvatech.uk.com , www.halvion.co.uk, www.truvexa.com/professional/, www.zul.com, www.mivlen.com,

Best to message me if you have any questions

Target Market(s)

small to medium UK based companies that require IT support services

Industry/Entity Type

It Company

Contact Information for Business Card

use dummy name, telephone and email for now, will provide details later.

Logo Text

bryn calvo (and then below the logo it should say "your IT, networks and security partner")

Coding

Coded - Design and coding required

Number of Pages Required

5+ page

Colors

Designer to choose colors to be used in the design.

Requirements
Must have
• must be professional, yet simple and clear that this is a serious IT support and IT security company.
Nice to have
• 1)The website homepage must have professional quality pictures of IT support or London city skyline or any picture that projects friendly business partners, professionalism and ready to serve.
• 2) Home page needs to include tabs for following pages 'Services' , 'About Us' , 'Contact Us' 'Home'
• 3) Website built customised using wordpress is ideal and easy for us to manage.
• more room for boxed options from homepage (with pic or image in background)
Should not have
• no checkout trolleys or payment options.

```html
<!DOCTYPE html>
<html lang="en">
<head>
<meta charset="utf-8">
<title>Bryn Calvo – IT Support &amp; Security</title>
<link href="https://fonts.googleapis.com/css2?family=Roboto:wght@400;500;700;900&family=Poppins:wght@500&display=swap" rel="stylesheet">
<style>
:root{
  --blue:#1a6fc4;
  --blue-dark:#0f57a3;
  --navy:#1d4f91;
  --ink:#2b2b2b;
  --text:#555;
  --cyan:#3fbfdc;
  --green:#169a45;
  --amber:#f7b73a;
  --orange:#f26a21;
  --grey:#f1f1f1;
  --line:#dcdcdc;
}
*{margin:0;padding:0;box-sizing:border-box}
html,body{width:1200px;height:3015px;overflow:hidden;background:#fff}
body{position:relative;font-family:"Roboto",Arial,sans-serif;color:var(--text)}
.abs{position:absolute}

/* header */
.brand{left:100px;top:26px;display:flex;align-items:center;gap:14px}
.brand-dot{width:70px;height:70px;border-radius:50%;background:var(--blue)}
.brand-name{font-size:40px;font-weight:700;color:var(--ink);line-height:1}
.brand-tag{font-size:17px;color:var(--ink);margin-top:6px}
.call{left:666px;top:46px;display:flex;gap:8px;align-items:center}
.call-text{font-size:16px;color:var(--ink);line-height:1.15}
.call-text b{font-weight:500;font-size:18px}
.login{left:866px;top:46px;width:106px;height:36px;background:var(--blue);color:#fff;font-size:15px;font-weight:500;display:flex;align-items:center;justify-content:center;border-radius:2px}
.social{left:996px;top:46px;display:flex;gap:4px}
.social span{width:32px;height:32px;border-radius:50%;background:var(--blue-dark)}
.social span:nth-child(2){background:#2a2a2a}

/* nav */
.nav{left:98px;top:140px;width:1002px;height:56px;background:linear-gradient(#2a86db,#1666b8);display:flex;align-items:center}
.nav a{color:#fff;text-decoration:none;font-size:16px;font-weight:500;height:56px;display:flex;align-items:center;padding:0 30px;border-right:1px solid rgba(255,255,255,.15)}
.nav a.active{background:#0d57a6}
.search{left:870px;top:150px;width:216px;height:34px;background:#fff;border-radius:17px;font-size:11px;color:#999;padding:0 14px;display:flex;align-items:center;justify-content:space-between}

/* hero */
.hero-band{left:0;top:196px;width:1200px;height:504px;background:#eeeeee}
.hero{left:98px;top:196px;width:1002px;height:504px;background:linear-gradient(180deg,#4a4d5e 0%,#b98a5a 30%,#e8b46a 45%,#6b5f58 60%,#3b5a78 80%,#2b4c69 100%);box-shadow:0 20px 30px -18px rgba(0,0,0,.45)}
.hero-title{left:392px;top:430px;width:414px;height:90px;border:3px solid #fff;color:#fff;font-size:58px;font-weight:900;display:flex;align-items:center;justify-content:center;letter-spacing:1px}
.dots{left:566px;top:646px;display:flex;gap:5px}
.dots span{width:14px;height:14px;border:2px solid #fff;border-radius:50%}

/* welcome */
.welcome-h{left:0;top:756px;width:1200px;text-align:center;font-size:40px;font-weight:500;color:var(--ink)}
.welcome-p{left:135px;top:820px;width:930px;text-align:center;font-size:12.5px;line-height:25px;color:var(--text)}

/* service boxes */
.box{top:1012px;width:328px;height:250px;color:#fff;text-align:center}
.box.cyan{left:98px;background:var(--cyan)}
.box.green{left:436px;background:var(--green)}
.box.amber{left:773px;background:var(--amber)}
.box-icon{position:absolute;left:114px;top:-44px;width:100px;height:100px;border-radius:50%;background:#fff;border:5px solid currentColor;display:flex;align-items:center;justify-content:center}
.cyan .box-icon{color:var(--cyan)}.green .box-icon{color:var(--green)}.amber .box-icon{color:var(--amber)}
.box h3{margin-top:86px;font-size:18px;font-weight:500;text-transform:uppercase;color:#fff}
.box p{margin:10px 18px 0;font-size:12.5px;line-height:22px}
.box .more{margin-top:14px;font-size:12px;font-weight:500}

/* support section */
.support{left:0;top:1352px;width:1200px;height:448px;background:var(--grey)}
.support-photo{left:0;top:1352px;width:600px;height:448px;background:linear-gradient(90deg,#dfe3e6 0%,#c9d2d8 45%,#9aa3ab 75%,#f1f1f1 100%)}
.support-h{left:652px;top:1458px;font-size:32px;font-weight:500;color:var(--ink)}
.support-p{left:652px;top:1512px;width:450px;font-size:12.5px;line-height:27px}
.btn{left:652px;top:1650px;width:112px;height:32px;background:var(--navy);color:#fff;font-size:13px;display:flex;align-items:center;justify-content:center}

/* news */
.news-h{left:0;top:1874px;width:1200px;text-align:center;font-size:32px;font-weight:500;color:var(--ink)}
.card{top:1953px;width:314px;height:298px;border-bottom:3px solid #ddd}
.card-img{width:314px;height:197px}
.card .date{position:absolute;left:12px;top:212px;width:58px;height:58px;border-radius:50%;background:var(--orange);color:#fff;font-size:10px;line-height:14px;text-align:center;padding-top:15px}
.card h4{position:absolute;left:80px;top:214px;font-family:"Poppins",sans-serif;font-weight:500;font-size:15.5px;color:var(--ink)}
.card p{position:absolute;left:80px;top:240px;width:220px;font-size:12px;line-height:18px}

/* partners */
.partners{left:0;top:2352px;width:1200px;height:290px;background:var(--green)}
.partners-h{left:0;top:2378px;width:1200px;text-align:center;font-size:32px;font-weight:500;color:#fff}
.pbox{top:2455px;width:188px;height:84px;background:#fff;display:flex;align-items:center;justify-content:center}
.pbox span{width:110px;height:30px;background:#c9c9c9;border-radius:3px}

/* footer */
.footer{left:0;top:2620px;width:1200px;height:322px;background:#f3f3f3}
.f-brand{left:98px;top:2708px;width:162px;text-align:center}
.f-brand .dot{width:64px;height:64px;border-radius:50%;background:var(--blue);margin:0 auto 12px}
.f-brand b{display:block;font-size:30px;font-weight:700;color:var(--ink)}
.f-brand small{display:block;font-size:14px;color:var(--ink);margin-top:4px}
.f-social{display:flex;justify-content:center;gap:5px;margin-top:10px}
.f-social span{width:22px;height:22px;border-radius:50%;border:2px solid var(--blue)}
.f-h{top:2706px;font-size:19px;font-weight:500;color:var(--ink);text-transform:uppercase}
.f-list{left:310px;top:2758px;font-size:13px;line-height:20px;color:var(--ink)}
.f-list li{list-style:none;display:flex;gap:14px;margin-bottom:12px}
.f-news-p{left:615px;top:2750px;width:290px;font-size:11.5px;line-height:19px}
.f-input{left:615px;top:2800px;width:296px;height:40px;background:#fff;border:1px solid var(--line);font-size:11px;color:#888;padding:0 14px;display:flex;align-items:center}
.f-btn{left:615px;top:2850px;width:120px;height:38px;background:var(--blue);color:#fff;font-weight:500;font-size:15px;display:flex;align-items:center;justify-content:center}
.f-links{left:970px;top:2746px;font-size:13px;color:var(--ink);line-height:24px}
.f-links li{list-style:none}
.f-links li::before{content:"▸ ";font-size:10px}
.copy{left:0;top:2942px;width:1200px;height:73px;border-top:1px solid var(--line);text-align:center;font-size:12px;line-height:73px;color:var(--ink)}
</style>
</head>
<body>

<header>
  <div class="abs brand">
    <span class="brand-dot"></span>
    <div><div class="brand-name">Bryn Calvo</div><div class="brand-tag">IT Support &amp; Security</div></div>
  </div>
  <div class="abs call">
    <svg width="28" height="28" viewBox="0 0 24 24"><path fill="#1d4f91" d="M6.6 10.8a15 15 0 0 0 6.6 6.6l2.2-2.2a1 1 0 0 1 1-.25 11 11 0 0 0 3.6.6 1 1 0 0 1 1 1V20a1 1 0 0 1-1 1A17 17 0 0 1 3 4a1 1 0 0 1 1-1h3.5a1 1 0 0 1 1 1c0 1.25.2 2.45.6 3.6a1 1 0 0 1-.25 1z"/></svg>
    <div class="call-text">Call Us:<br><b>1-808-555-0192</b></div>
  </div>
  <div class="abs login">LOGIN</div>
  <div class="abs social"><span></span><span></span><span></span></div>
</header>

<nav class="abs nav">
  <a class="active">HOME</a><a>SERVICES</a><a>ABOUT US</a><a>CONTACT US</a>
</nav>
<div class="abs search">Search
  <svg width="12" height="12" viewBox="0 0 24 24"><circle cx="10" cy="10" r="7" fill="none" stroke="#555" stroke-width="3"/><path d="M15 15l6 6" stroke="#555" stroke-width="3"/></svg>
</div>

<div class="abs hero-band"></div>
<div class="abs hero" role="img" aria-label="London skyline at dusk with the river and a clock tower"></div>
<div class="abs hero-title">BRYN CALVO</div>
<div class="abs dots"><span></span><span></span><span></span><span></span></div>

<h1 class="abs welcome-h">Welcome To Bryn Calvo</h1>
<p class="abs welcome-p">We keep the systems of small and medium UK firms running smoothly, safely and without fuss. Our team handles support desks, network care, backups and security checks so your staff can focus on the work that matters. From a single office to several sites, we plan, install and watch over your technology with clear advice, fair prices and fast response times, day or night, wherever your people happen to be working this week.</p>

<section>
  <div class="abs box cyan">
    <div class="box-icon"><svg width="46" height="40" viewBox="0 0 46 40"><rect x="2" y="2" width="42" height="28" rx="2" fill="none" stroke="currentColor" stroke-width="3"/><path d="M9 22l8-8 6 6 12-10" fill="none" stroke="currentColor" stroke-width="3"/><path d="M16 37h14M23 30v7" stroke="currentColor" stroke-width="3"/></svg></div>
    <h3>Business Continuity</h3>
    <p>Keep trading through outages with tested backups, recovery plans and secure remote access for every member of your team.</p>
    <div class="more">READ MORE ➜</div>
  </div>
  <div class="abs box green">
    <div class="box-icon"><svg width="44" height="44" viewBox="0 0 44 44"><path d="M8 36L30 14M14 8l22 22" stroke="currentColor" stroke-width="5" stroke-linecap="round"/><circle cx="32" cy="10" r="6" fill="none" stroke="currentColor" stroke-width="4"/></svg></div>
    <h3>IT Support &amp; Field Services</h3>
    <p>Friendly engineers on site and online, fixing faults, setting up kit and keeping your office network in good order.</p>
    <div class="more">READ MORE ➜</div>
  </div>
  <div class="abs box amber">
    <div class="box-icon"><svg width="36" height="44" viewBox="0 0 36 44"><path d="M8 20V12a10 10 0 0 1 19-4" fill="none" stroke="currentColor" stroke-width="4"/><rect x="2" y="20" width="32" height="22" rx="3" fill="currentColor"/></svg></div>
    <h3>Outsourced Service Desk</h3>
    <p>A dedicated help desk that answers your calls, logs every ticket and resolves issues quickly in plain English.</p>
    <div class="more">READ MORE ➜</div>
  </div>
</section>

<section>
  <div class="abs support"></div>
  <div class="abs support-photo" role="img" aria-label="Business team meeting around a laptop with charts on a board"></div>
  <h2 class="abs support-h">IT SUPPORT &amp; SECURITY</h2>
  <p class="abs support-p">We protect your data, devices and people with layered security, regular patching and round the clock monitoring. Our specialists review risks, train staff and respond to threats before they spread, giving you calm, dependable IT that grows with your business.</p>
  <div class="abs btn">READ MORE</div>
</section>

<section>
  <h2 class="abs news-h">LATEST NEWS</h2>
  <article class="abs card" style="left:98px">
    <div class="card-img" role="img" aria-label="Engineer with a laptop in a server room" style="background:linear-gradient(135deg,#4a6f8c,#c8d4dc)"></div>
    <div class="date">APR 05<br>2018</div>
    <h4>Nemo enim ipsam volupta</h4>
    <p>Simple steps to keep your office network safe</p>
  </article>
  <article class="abs card" style="left:440px">
    <div class="card-img" role="img" aria-label="Hands typing on a laptop keyboard" style="background:linear-gradient(135deg,#e9e9e9,#8c8c8c)"></div>
    <div class="date">APR 05<br>2018</div>
    <h4>Nemo enim ipsam volupta</h4>
    <p>Why regular backups matter for growing teams</p>
  </article>
  <article class="abs card" style="left:782px">
    <div class="card-img" role="img" aria-label="Person viewing a large digital data display" style="background:linear-gradient(135deg,#1e2a3a,#5d7189)"></div>
    <div class="date">APR 05<br>2018</div>
    <h4>Nemo enim ipsam volupta</h4>
    <p>New service desk hours for all our clients</p>
  </article>
</section>

<section>
  <div class="abs partners"></div>
  <h2 class="abs partners-h">PARTNERS</h2>
  <svg class="abs" style="left:52px;top:2478px" width="20" height="40" viewBox="0 0 20 40"><path d="M16 4L4 20l12 16" fill="none" stroke="#fff" stroke-width="2"/></svg>
  <svg class="abs" style="left:1128px;top:2478px" width="20" height="40" viewBox="0 0 20 40"><path d="M4 4l12 16L4 36" fill="none" stroke="#fff" stroke-width="2"/></svg>
  <div class="abs pbox" style="left:98px"><span></span></div>
  <div class="abs pbox" style="left:302px"><span></span></div>
  <div class="abs pbox" style="left:506px"><span></span></div>
  <div class="abs pbox" style="left:710px"><span></span></div>
  <div class="abs pbox" style="left:914px"><span></span></div>
</section>

<footer>
  <div class="abs footer"></div>
  <svg class="abs" style="left:0;top:2570px" width="1200" height="80" viewBox="0 0 1200 80" preserveAspectRatio="none">
    <path d="M0 80V40C300 -5 700 10 1200 30V80Z" fill="#f3f3f3"/>
    <path d="M0 38C300 -8 700 8 1200 28" fill="none" stroke="#fff" stroke-width="6"/>
  </svg>
  <div class="abs f-brand">
    <div class="dot"></div>
    <b>Bryn Calvo</b>
    <small>IT Support &amp; Security</small>
    <div class="f-social"><span></span><span></span><span></span><span></span></div>
  </div>

  <h3 class="abs f-h" style="left:310px">Contact Us</h3>
  <ul class="abs f-list">
    <li><svg width="12" height="16" viewBox="0 0 12 16"><path d="M6 0a6 6 0 0 0-6 6c0 4.5 6 10 6 10s6-5.5 6-10a6 6 0 0 0-6-6z" fill="#1a6fc4"/><circle cx="6" cy="6" r="2" fill="#fff"/></svg><span>400 Bryn Calvo<br>Street, Suite 201 Larkfield, MA 02190</span></li>
    <li><svg width="12" height="14" viewBox="0 0 24 24"><path fill="#1a6fc4" d="M6.6 10.8a15 15 0 0 0 6.6 6.6l2.2-2.2a1 1 0 0 1 1-.25 11 11 0 0 0 3.6.6 1 1 0 0 1 1 1V20a1 1 0 0 1-1 1A17 17 0 0 1 3 4a1 1 0 0 1 1-1h3.5a1 1 0 0 1 1 1c0 1.25.2 2.45.6 3.6a1 1 0 0 1-.25 1z"/></svg><span>Phone: 781-555-0147</span></li>
    <li><svg width="12" height="14" viewBox="0 0 12 10"><rect width="12" height="10" fill="#1a6fc4"/><path d="M0 0l6 5 6-5" fill="none" stroke="#fff"/></svg><span>info@bryncalvo.com</span></li>
  </ul>

  <h3 class="abs f-h" style="left:615px">Sign Up For Newsletter</h3>
  <p class="abs f-news-p">Get short monthly tips on support, backups and staying secure online.</p>
  <div class="abs f-input">Enter email</div>
  <div class="abs f-btn">SIGN UP</div>

  <h3 class="abs f-h" style="left:970px">Quick Links</h3>
  <ul class="abs f-links"><li>Home</li><li>About</li><li>Services</li><li>Contact us</li></ul>

  <div class="abs copy">© Copyright 2018 Bryn Calvo. All Rights Reserved.</div>
</footer>

</body>
</html>
```